Fitness Business Card Design Needed

We are looking for a business card design that stands out but is also simple and unique. I like the idea of on one side using the picture of myself with my logo at my feet. I love the texture on the business card so please take that into account when designing. Then on the other side having my contact details. I want it to be clean, modern, and pretty. I am open to designs that allow spot gloss or gold foiling.

Space for Name, Phone number, email, and website

```html
<!DOCTYPE html>
<html lang="en">
<head>
<meta charset="utf-8">
<title>Halcyon Strength – Business Card</title>
<link rel="stylesheet" href="https://fonts.googleapis.com/css2?family=Montserrat:wght@400&family=Roboto:wght@300;400&display=swap">
<style>
  :root {
    --backdrop: #8a8a8a;
    --card-yellow: #e9b860;
    --card-white: #f4f4f2;
    --gold: #b98b3a;
    --gold-light: #d4a850;
    --ink: #1e1e1e;
    --grey-text: #4a4a4a;
    --rule: #a9a9a9;
    --photo-warm: #c98e68;
    --photo-coral: #d9604a;
  }
  * { box-sizing: border-box; margin: 0; padding: 0; }
  html, body { width: 1200px; height: 1200px; overflow: hidden; }
  body { background: var(--backdrop); position: relative; font-family: "Roboto", sans-serif; }

  .card {
    position: absolute;
    top: 311px;
    width: 369px;
    height: 592px;
    overflow: hidden;
    box-shadow: 2px 4px 8px rgba(0,0,0,0.35);
  }
  .card--front {
    left: 234px;
    background-color: var(--card-yellow);
    background-image:
      repeating-linear-gradient(0deg, rgba(255,255,255,0.05) 0 1px, transparent 1px 4px),
      repeating-linear-gradient(90deg, rgba(0,0,0,0.04) 0 1px, transparent 1px 4px);
  }
  .card--back {
    left: 646px;
    width: 364px;
    background-color: var(--card-white);
    background-image:
      repeating-linear-gradient(0deg, rgba(0,0,0,0.025) 0 1px, transparent 1px 4px),
      repeating-linear-gradient(90deg, rgba(0,0,0,0.02) 0 1px, transparent 1px 4px);
    text-align: center;
  }

  .portrait {
    position: absolute;
    left: 108px;
    top: 14px;
    width: 261px;
    height: 578px;
    border-radius: 120px 120px 0 0;
    background: linear-gradient(180deg, #d9c7b0 0%, var(--photo-warm) 22%, var(--photo-coral) 42%, var(--photo-warm) 55%, var(--photo-coral) 66%, #b97a58 100%);
    opacity: 0.85;
  }

  .brand-vertical {
    position: absolute;
    left: 38px;
    top: 94px;
    width: 40px;
    height: 400px;
    writing-mode: vertical-rl;
    transform: rotate(180deg);
    text-align: center;
    font-family: "Montserrat", sans-serif;
    font-weight: 400;
    font-size: 28px;
    letter-spacing: 2px;
    line-height: 40px;
    white-space: nowrap;
    color: var(--ink);
  }

  .contact-name {
    margin-top: 78px;
    font-size: 22px;
    font-weight: 400;
    color: var(--gold);
    letter-spacing: 0.3px;
  }
  .contact-title {
    font-size: 16px;
    font-weight: 300;
    color: var(--grey-text);
    letter-spacing: 0.6px;
    margin-top: 2px;
  }
  .icon-row {
    display: flex;
    align-items: center;
    justify-content: center;
    gap: 4px;
    margin-top: 20px;
  }
  .icon-row__rule { width: 48px; height: 1px; background: var(--rule); margin: 0 8px; }
  .icon-row svg { display: block; }

  .contact-list { list-style: none; margin-top: 8px; }
  .contact-list li {
    font-size: 16px;
    font-weight: 300;
    color: var(--grey-text);
    line-height: 21.5px;
    letter-spacing: 0.2px;
  }

  .brand-block {
    position: absolute;
    left: 0;
    right: 0;
    top: 500px;
    font-family: "Montserrat", sans-serif;
    font-weight: 400;
    font-size: 22px;
    letter-spacing: 1.5px;
    line-height: 28px;
    color: var(--ink);
  }
</style>
</head>
<body>

  <section class="card card--front">
    <div class="portrait" role="img" aria-label="Full-length portrait photo of the fitness trainer standing with hands on hips"></div>
    <p class="brand-vertical">HALCYON STRENGTH</p>
  </section>

  <section class="card card--back">
    <h1 class="contact-name">DANIEL BROOKS</h1>
    <p class="contact-title">MANAGING DIRECTOR</p>

    <div class="icon-row">
      <span class="icon-row__rule"></span>
      <svg width="22" height="22" viewBox="0 0 22 22" aria-label="Phone">
        <circle cx="11" cy="11" r="11" fill="var(--gold-light)"/>
        <path d="M7.5 6.5c.6-.5 1.3-.4 1.6.2l.8 1.5c.2.5 0 1-.4 1.3l-.5.4c.5 1.2 1.4 2.1 2.6 2.6l.4-.5c.3-.4.8-.6 1.3-.4l1.5.8c.6.3.7 1 .2 1.6-.9 1-2.2 1.1-3.4.5-1.9-.9-3.4-2.4-4.3-4.3-.6-1.2-.5-2.5.5-3.4z" fill="#fff"/>
      </svg>
      <svg width="22" height="22" viewBox="0 0 22 22" aria-label="Email">
        <circle cx="11" cy="11" r="11" fill="var(--gold-light)"/>
        <rect x="6" y="7.5" width="10" height="7" fill="#fff"/>
        <path d="M6 7.5l5 4 5-4" fill="none" stroke="var(--gold-light)" stroke-width="1"/>
      </svg>
      <svg width="22" height="22" viewBox="0 0 22 22" aria-label="Website">
        <circle cx="11" cy="11" r="11" fill="var(--gold-light)"/>
        <circle cx="11" cy="11" r="5" fill="none" stroke="#fff" stroke-width="1.3"/>
        <path d="M6 11h10M11 6c-2 2.8-2 7.2 0 10M11 6c2 2.8 2 7.2 0 10" fill="none" stroke="#fff" stroke-width="1"/>
      </svg>
      <span class="icon-row__rule"></span>
    </div>

    <ul class="contact-list">
      <li>055-987 654 321</li>
      <li>HELLO@HALCYONSTRENGTH.COM</li>
      <li>WWW.HALCYONSTRENGTH.COM</li>
    </ul>

    <p class="brand-block">HALCYON STRENGTH</p>
  </section>

</body>
</html>
```